Private Investment Partnership needs Business Card Design

We are a brand-new private investment partnership looking for business card design help. It will be called The Corvale + Vantry Partnership. We are based in NYC (hence Corvale) and our other partner is a firm called Vantry Resources which has roots in Pittsburgh, PA. We are looking for something a bit more formal and professional- probably typographic oriented in a font like Adobe Garamond. We might want to incorporate the colors PMS Yellow 1235 and PMS Blue 282. Attached is a pretty plain, old example of something.

```html
<!DOCTYPE html>
<html lang="en">
<head>
<meta charset="utf-8">
<title>Corvale Vantry Capital – Business Card</title>
<link rel="stylesheet" href="https://fonts.googleapis.com/css2?family=EB+Garamond:wght@400;600;700&display=swap">
<style>
  :root {
    --navy: #172036;
    --gold: #e8b021;
    --muted: #9aa3b6;
    --rule: #5b6478;
    --backdrop: #e4e4e4;
  }
  html, body {
    margin: 0;
    width: 1200px;
    height: 1200px;
    overflow: hidden;
    background: var(--backdrop);
  }
  .card {
    position: absolute;
    left: 75px;
    top: 300px;
    width: 1050px;
    height: 600px;
    background: var(--navy);
    font-family: "EB Garamond", Garamond, serif;
    box-shadow: 0 10px 30px rgba(0,0,0,0.18);
  }
  .company {
    position: absolute;
    right: 80px;
    top: 118px;
    margin: 0;
    color: var(--gold);
    font-size: 46px;
    font-weight: 600;
    letter-spacing: 1px;
    text-transform: uppercase;
  }
  .band {
    position: absolute;
    left: 0;
    right: 0;
    top: 215px;
    height: 72px;
    background: var(--gold);
    display: flex;
    align-items: center;
    padding-left: 72px;
    color: var(--navy);
  }
  .band .person {
    font-size: 31px;
    font-weight: 700;
    text-transform: uppercase;
    letter-spacing: 0.5px;
  }
  .band .divider {
    width: 2px;
    height: 34px;
    background: var(--navy);
    opacity: 0.35;
    margin: 0 18px;
  }
  .band .role {
    font-size: 23px;
    text-transform: uppercase;
    letter-spacing: 0.5px;
  }
  .address {
    position: absolute;
    left: 100px;
    top: 312px;
    color: var(--muted);
    font-size: 23px;
    line-height: 30px;
    text-transform: uppercase;
  }
  .line {
    display: flex;
    align-items: center;
    gap: 10px;
  }
  .email {
    position: absolute;
    left: 72px;
    top: 380px;
    color: var(--muted);
    font-size: 24px;
  }
  .rule {
    position: absolute;
    left: 560px;
    top: 320px;
    width: 2px;
    height: 110px;
    background: var(--rule);
  }
  .phones {
    position: absolute;
    left: 590px;
    top: 355px;
    color: var(--muted);
    font-size: 24px;
    line-height: 36px;
  }
  .icon { width: 22px; height: 22px; flex: none; }
</style>
</head>
<body>
  <div class="card">
    <h1 class="company">Corvale Vantry Capital, LLC</h1>

    <div class="band">
      <span class="person">Daniel R. Mercer</span>
      <span class="divider"></span>
      <span class="role">Chief Investment Officer</span>
    </div>

    <div class="address">
      <div>418 East Harbor Avenue,</div>
      <div>Westbrook, CT 06498</div>
    </div>

    <div class="email line">
      <svg class="icon" viewBox="0 0 22 22" aria-hidden="true">
        <circle cx="11" cy="11" r="11" fill="var(--gold)"/>
        <rect x="5" y="7" width="12" height="8" fill="none" stroke="var(--navy)" stroke-width="1.5"/>
        <path d="M5 7 L11 12 L17 7" fill="none" stroke="var(--navy)" stroke-width="1.5"/>
      </svg>
      <span>dmercer@corvalevantry.com</span>
    </div>

    <div class="rule"></div>

    <div class="phones">
      <div class="line">
        <svg class="icon" viewBox="0 0 22 22" aria-hidden="true">
          <circle cx="11" cy="11" r="11" fill="var(--gold)"/>
          <rect x="6" y="7" width="10" height="9" rx="1.5" fill="none" stroke="var(--navy)" stroke-width="1.5"/>
          <path d="M7 7 Q11 3 15 7" fill="none" stroke="var(--navy)" stroke-width="1.5"/>
        </svg>
        <span>(203) 555-0148</span>
      </div>
      <div class="line">
        <svg class="icon" viewBox="0 0 22 22" aria-hidden="true">
          <circle cx="11" cy="11" r="11" fill="var(--gold)"/>
          <rect x="7.5" y="5" width="7" height="12" rx="1.2" fill="none" stroke="var(--navy)" stroke-width="1.5"/>
          <circle cx="11" cy="14.5" r="0.9" fill="var(--navy)"/>
        </svg>
        <span>(646) 555-0192</span>
      </div>
    </div>
  </div>
</body>
</html>
```